ebook cover for book three in a spiritual iconic series: bold, simple, easy to manage!

The Hollow is the third in a series of memoirs about one woman's spiritual journey over ten years. A PhD, the woman wants to appeal to a broad market and an intellectual market as well as the women's market that makes the core audience. Any Old Kettle is the second book and its cover is currently also commissioned here on Pixel Market if you want to search it. We Grow Radish was the first and its cover is attached for your reference. Please keep the same: the white background, the shade of red for the title, the font for the subtitle and colour, but change the title font and how you use the colour scheme. We look for a slightly enigmatic and also strikingly simple image. The tin can in We Grow Radish is where to start. For Any Old Kettle we have asked for a single Wordlark tablet, the X. Here, we are thinking of the winking smiley attached, but the image needs some photoshopping to make the face a bit more to yellow cold, remove the red ring and so on. The colours to pick from are greys, purple, red, orange, yellow, as with the colors in the flash of light on the tin can in Grow Radish. The idea there was to capture an explosion to new ideas while referencing a key scene involving cooking with tomatoes!

The Hollow

Book details:
Title: The Hollow
Subtitle: Brother Osric presents Veldora
Image ideas: Winking smiley attached, princess castle in the right colours, magic wand.
Author: Marla Quince, Ph.D
Strap quote: "Marla Quince is phenomenal in the true sense of the word. Phenomenons occur around her," Paula Drent, Teacher and spiritual healer

```html
<!DOCTYPE html>
<html lang="en">
<head>
<meta charset="utf-8">
<title>The Hollow — Marla Quince Ph.D.</title>
<link rel="stylesheet" href="https://fonts.googleapis.com/css2?family=Oswald:wght@600&family=Open+Sans:wght@400;600;700&display=swap">
<style>
  :root {
    --paper: #ffffff;
    --title-red-top: #c40d0d;
    --title-red-bottom: #9c1c1c;
    --ink: #2b2b2b;
    --author-grey: #6a6a6a;
    --sun-core: #fff36a;
    --sun-mid: #fde52a;
    --sun-edge: #f3d80e;
  }
  html, body {
    margin: 0;
    padding: 0;
    overflow: hidden;
    background: var(--paper);
  }
  .cover {
    position: relative;
    width: 800px;
    height: 1200px;
    background: var(--paper);
    overflow: hidden;
  }
  .strap-quote {
    position: absolute;
    top: 44px;
    left: 40px;
    width: 720px;
    margin: 0;
    text-align: center;
    font-family: "Open Sans", sans-serif;
    font-weight: 600;
    font-size: 15px;
    line-height: 26px;
    letter-spacing: 0.2px;
    text-transform: uppercase;
    color: #111;
  }
  .strap-quote .quote-source {
    font-weight: 700;
    font-size: 17px;
    letter-spacing: 0.6px;
    color: var(--ink);
  }
  .book-title {
    position: absolute;
    top: 128px;
    left: 0;
    width: 800px;
    margin: 0;
    text-align: center;
    white-space: nowrap;
    font-family: "Oswald", sans-serif;
    font-weight: 600;
    font-size: 140px;
    line-height: 170px;
    letter-spacing: 2px;
    text-transform: uppercase;
    background: linear-gradient(180deg, var(--title-red-top), var(--title-red-bottom));
    -webkit-background-clip: text;
    background-clip: text;
    color: transparent;
  }
  .subtitle {
    position: absolute;
    top: 318px;
    left: 0;
    width: 800px;
    margin: 0;
    text-align: center;
    font-family: "Open Sans", sans-serif;
    font-weight: 600;
    font-size: 31px;
    line-height: 47px;
    letter-spacing: 4px;
    text-transform: uppercase;
    color: var(--ink);
  }
  .cover-art {
    position: absolute;
    top: 430px;
    left: 140px;
    width: 520px;
    height: 540px;
  }
  .author {
    position: absolute;
    top: 1064px;
    left: 0;
    width: 800px;
    margin: 0;
    text-align: center;
    font-family: "Open Sans", sans-serif;
    font-weight: 400;
    font-size: 42px;
    line-height: 60px;
    letter-spacing: 3px;
    text-transform: uppercase;
    color: var(--author-grey);
  }
</style>
</head>
<body>
  <main class="cover">
    <p class="strap-quote">"Marla Quince is phenomenal in the true sense of the word. Phenomenons<br>occur around her" - <span class="quote-source">Paula Drent, Teacher and Spiritual Healer</span></p>

    <h1 class="book-title">The Hollow</h1>

    <h2 class="subtitle">Brother Osric<br>presents Veldora</h2>

    <svg class="cover-art" viewBox="0 0 520 540" role="img" aria-label="Glowing yellow winking smiley illustration with a flash of light at its upper left">
      <defs>
        <radialGradient id="sun-glow" cx="0.38" cy="0.3" r="0.75">
          <stop offset="0" stop-color="var(--sun-core)"/>
          <stop offset="0.6" stop-color="var(--sun-mid)"/>
          <stop offset="1" stop-color="var(--sun-edge)"/>
        </radialGradient>
        <radialGradient id="light-flash" cx="0.5" cy="0.5" r="0.5">
          <stop offset="0" stop-color="#ffffff" stop-opacity="1"/>
          <stop offset="0.4" stop-color="#ffffff" stop-opacity="0.7"/>
          <stop offset="1" stop-color="#ffffff" stop-opacity="0"/>
        </radialGradient>
      </defs>
      <circle class="smiley-disc" cx="260" cy="288" r="243" fill="url(#sun-glow)"/>
      <circle class="flash" cx="105" cy="110" r="90" fill="url(#light-flash)"/>
    </svg>

    <p class="author">Marla Quince Ph.D.</p>
  </main>
</body>
</html>
```